Business Card Design For Marketing Agnecy LWP

Need business card design for marketing agency.

Dorian Pellow
President, CEO
1-555-302-4196
dorian@brightlanepromotions.example
www.BrightlanePromotions.example

Back Side:
Boost Sales Using Rewards, Incentives & Giveaways
Get A Free Sample Package

Target Market(s)

B2B

Industry/Entity Type

Marketing

Contact Information for Business Card

Dorian Pellow
President, CEO
1-555-302-4196

Back Side:
Get A Free Sample Package

Please note that my current url is OLD DESIGN. I am working on new design and want the business card to match color themes at least on new site. Here is the demo link for new site so you can see the colors I use, etc.

http://pixelquarrydemo.example/dh/dorian/lwp_final/index.html

Requirements
Must have
• Please note that my current url is OLD DESIGN. I am working on new design and want the business card to match color themes at least on new site. Here is the demo link for new site so you can see the colors I use, etc.

Nice to have

Should not have

```html
<!DOCTYPE html>
<html lang="en">
<head>
<meta charset="utf-8">
<title>Brightlane Promotions Business Card – Front and Back</title>
<link href="https://fonts.googleapis.com/css2?family=Poppins:wght@400;500;600;700;800&display=swap" rel="stylesheet">
<style>
  :root {
    --brand-blue: #1f73c0;
    --ink-grey: #4a4a4c;
    --band-grey: #58595b;
    --paper: #ffffff;
    --paper-soft: #f3f3f3;
    --stage: #e6e7e9;
  }
  * { box-sizing: border-box; margin: 0; padding: 0; }
  html, body {
    width: 1200px; height: 900px; overflow: hidden;
    background: var(--stage);
    font-family: "Poppins", sans-serif;
  }
  .stage {
    width: 1200px; height: 900px;
    display: flex; flex-direction: column; align-items: center; justify-content: center;
    gap: 56px;
  }
  .card {
    position: relative;
    width: 560px; height: 320px;
    background: var(--paper);
    overflow: hidden;
    box-shadow: 0 10px 26px rgba(0,0,0,.18);
  }

  /* Company name */
  .brand {
    position: absolute; left: 44px; top: 46px;
    display: flex; align-items: center; gap: 10px;
  }
  .brand-mark {
    width: 12px; height: 12px; background: var(--brand-blue); flex: none;
  }
  .brand-name {
    font-weight: 500; font-size: 24px; line-height: 1.1;
    color: var(--brand-blue);
  }

  /* Front */
  .identity {
    position: absolute; right: 44px; top: 142px;
    display: flex; align-items: center; gap: 12px;
  }
  .identity-text { text-align: right; }
  .person-name {
    font-weight: 700; font-size: 17px; color: var(--brand-blue);
    text-transform: uppercase; letter-spacing: -.2px;
  }
  .person-title {
    font-weight: 400; font-size: 11px; color: var(--ink-grey);
    text-transform: uppercase; letter-spacing: .3px;
  }
  .identity-bar { width: 10px; height: 36px; background: var(--ink-grey); }
  .contacts {
    position: absolute; right: 44px; bottom: 38px;
    list-style: none;
  }
  .contacts li {
    display: flex; justify-content: flex-end; align-items: center; gap: 10px;
    font-size: 12px; color: var(--ink-grey); line-height: 22px;
  }
  .contacts svg { width: 14px; height: 14px; fill: var(--brand-blue); flex: none; }

  /* Back */
  .back-top {
    position: absolute; left: 0; top: 0; width: 100%; height: 118px;
    background: var(--brand-blue);
  }
  .back-top .brand { left: auto; right: 48px; top: 42px; }
  .back-top .brand-name { color: var(--paper); font-size: 26px; }
  .back-top .brand-mark { background: var(--paper); }
  .back-message {
    position: absolute; left: 0; top: 118px; width: 100%; height: 126px;
    background: linear-gradient(180deg, var(--paper), var(--paper-soft));
    padding: 14px 34px 0;
    border-bottom: 5px solid var(--brand-blue);
  }
  .headline-lead {
    font-weight: 800; font-size: 24px; color: var(--ink-grey);
    text-transform: uppercase; line-height: 1.12;
  }
  .headline-main {
    font-weight: 500; font-size: 24px; color: var(--brand-blue);
    text-transform: uppercase; line-height: 1.12; letter-spacing: -.3px;
  }
  .offer { font-size: 14px; color: var(--ink-grey); margin-top: 4px; }
  .back-base {
    position: absolute; left: 0; bottom: 0; width: 100%; height: 76px;
    background: var(--band-grey);
  }
  .url-pill {
    position: absolute; left: 26px; top: 226px;
    background: var(--brand-blue); color: var(--paper);
    font-weight: 700; font-size: 18px; line-height: 28px;
    padding: 6px 26px; border-radius: 22px;
  }
</style>
</head>
<body>
<main class="stage">

  <section class="card card-front" aria-label="Business card front">
    <div class="brand">
      <span class="brand-mark"></span>
      <span class="brand-name">Brightlane Promotions</span>
    </div>

    <div class="identity">
      <div class="identity-text">
        <p class="person-name">Dorian Pellow</p>
        <p class="person-title">President, CEO</p>
      </div>
      <span class="identity-bar"></span>
    </div>

    <ul class="contacts">
      <li>1-555-302-4196
        <svg viewBox="0 0 24 24" aria-hidden="true"><path d="M6.6 10.8a15.1 15.1 0 0 0 6.6 6.6l2.2-2.2c.3-.3.7-.4 1-.2 1.1.4 2.3.6 3.6.6.6 0 1 .4 1 1V20c0 .6-.4 1-1 1A17 17 0 0 1 3 4c0-.6.4-1 1-1h3.5c.6 0 1 .4 1 1 0 1.3.2 2.5.6 3.6.1.3 0 .7-.2 1z"/></svg>
      </li>
      <li>dorian@brightlanepromotions.example
        <svg viewBox="0 0 24 24" aria-hidden="true"><path d="M2 5h20v14H2zm2 2v.5l8 5 8-5V7zm0 2.8V17h16V9.8l-8 5z"/></svg>
      </li>
      <li>www.BrightlanePromotions.example
        <svg viewBox="0 0 24 24" aria-hidden="true"><path d="M12 2a10 10 0 1 0 0 20 10 10 0 0 0 0-20zm6.9 6h-3a15 15 0 0 0-1.3-3.9A8 8 0 0 1 18.9 8zM12 4c.8 1.1 1.5 2.5 1.9 4h-3.8c.4-1.5 1.1-2.9 1.9-4zM4.3 14a8 8 0 0 1 0-4h3.4a16 16 0 0 0 0 4zm.8 2h3a15 15 0 0 0 1.3 3.9A8 8 0 0 1 5.1 16zm3-8h-3a8 8 0 0 1 4.3-3.9C8.8 5.3 8.4 6.6 8.1 8zM12 20c-.8-1.1-1.5-2.5-1.9-4h3.8c-.4 1.5-1.1 2.9-1.9 4zm2.3-6H9.7a14 14 0 0 1 0-4h4.6a14 14 0 0 1 0 4zm.3 5.9c.6-1.2 1-2.5 1.3-3.9h3a8 8 0 0 1-4.3 3.9zm1.7-5.9a16 16 0 0 0 0-4h3.4a8 8 0 0 1 0 4z"/></svg>
      </li>
    </ul>
  </section>

  <section class="card card-back" aria-label="Business card back">
    <div class="back-top">
      <div class="brand">
        <span class="brand-mark"></span>
        <span class="brand-name">Brightlane Promotions</span>
      </div>
    </div>

    <div class="back-message">
      <p class="headline-lead">Boost Sales &amp; Leads Using</p>
      <p class="headline-main">Rewards, Incentives &amp; Giveaways</p>
      <p class="offer">Get A Free Sample Package</p>
    </div>

    <div class="back-base"></div>
    <p class="url-pill">www.BrightlanePromotions.example</p>
  </section>

</main>
</body>
</html>
```